business cards, stationary
lets see what you got
Use specific fonts
up to designer
Modern
Calvin Marsh
Director of Sales
100 Example Street, Suite 1 Sampletown, ON A1A 1A1
Calvin@sunlanejourneys.example
www.sunlanejourneys.example
T: 905.555.0142
LOGO on back

```html
<!DOCTYPE html>
<html lang="en">
<head>
<meta charset="utf-8">
<title>Sunlane Journeys — Stationery Set</title>
<link rel="stylesheet" href="https://fonts.googleapis.com/css2?family=Poppins:wght@400;600;700&display=swap">
<style>
  :root {
    --purple: #3a2a7c;
    --green: #7cc242;
    --paper: #ffffff;
    --ink: #4a4a55;
    --ghost: #ececef;
    --stage: #e9e6e2;
  }
  * { box-sizing: border-box; margin: 0; padding: 0; }
  html, body { width: 1200px; height: 562px; overflow: hidden; }
  body {
    background: var(--stage);
    font-family: "Poppins", Arial, sans-serif;
    color: var(--ink);
    position: relative;
  }
  .sheet {
    position: absolute;
    background: var(--paper);
    overflow: hidden;
    box-shadow: 0 2px 6px rgba(0,0,0,.18);
  }
  .sheet svg.wave { position: absolute; left: 0; bottom: 0; width: 100%; }
  .brand {
    font-weight: 700;
    color: var(--green);
    letter-spacing: -0.02em;
    white-space: nowrap;
    display: inline-flex;
    align-items: center;
    gap: 4px;
  }
  .brand .dot { width: .8em; height: .8em; border-radius: 50%; background: currentColor; }
  .brand.on-dark { color: var(--paper); }

  /* business cards */
  .card { width: 158px; height: 96px; }
  .card-front { left: 29px; top: 96px; }
  .card-back-purple { left: 204px; top: 96px; background: var(--purple); }
  .card-back-white { left: 29px; top: 209px; }
  .card-back-green { left: 204px; top: 209px; background: var(--green); }
  .card .brand { position: absolute; left: 50%; transform: translateX(-50%); font-size: 10px; top: 40px; }
  .card-front .brand { top: 8px; }
  .card-person { position: absolute; left: 10px; top: 27px; font-size: 4.6px; line-height: 1.5; }
  .card-person strong { font-size: 5.6px; color: var(--purple); display: block; }
  .card-contact { position: absolute; left: 80px; top: 27px; font-size: 4.2px; line-height: 1.5; width: 72px; }

  /* letterhead */
  .letterhead { left: 365px; top: 29px; width: 398px; height: 506px; }
  .letterhead .brand { position: absolute; top: 26px; left: 50%; transform: translateX(-50%); font-size: 17px; }
  .ghost-mark {
    position: absolute; top: 210px; left: 50%; transform: translateX(-50%);
    font-size: 30px; font-weight: 700; color: var(--ghost); white-space: nowrap;
  }
  .footer-info {
    position: absolute; bottom: 20px; left: 18px; right: 18px;
    display: flex; gap: 30px; font-size: 5px; line-height: 1.5; color: var(--paper);
  }
  .footer-web { position: absolute; bottom: 4px; left: 0; right: 0; text-align: center; font-size: 4.5px; color: var(--paper); }

  /* envelope */
  .envelope { left: 782px; top: 29px; width: 394px; height: 199px; }
  .envelope .brand { position: absolute; top: 14px; left: 22px; font-size: 12px; }
  .envelope .ghost-mark { top: 60px; left: auto; right: 24px; transform: none; font-size: 20px; }
  .envelope .footer-info { bottom: 22px; font-size: 4.6px; }

  /* envelope flaps */
  .flap { position: absolute; left: 782px; width: 394px; height: 72px; }
  .flap svg { width: 100%; height: 100%; display: block; filter: drop-shadow(0 2px 2px rgba(0,0,0,.2)); }
  .flap .brand { position: absolute; top: 20px; left: 148px; font-size: 10px; }
  .flap-purple { top: 240px; }
  .flap-green { top: 336px; }
  .flap-white { top: 432px; }
</style>
</head>
<body>

  <!-- Business card front -->
  <section class="sheet card card-front">
    <span class="brand"><span class="dot"></span>sunlanejourneys</span>
    <div class="card-person">
      <strong>Calvin Marsh</strong>
      Director of Sales
    </div>
    <div class="card-contact">
      100 Example Street, Suite 1<br>Sampletown, ON A1A 1A1<br>
      Calvin@sunlanejourneys.example<br>www.sunlanejourneys.example<br>T: 905.555.0142
    </div>
    <svg class="wave" viewBox="0 0 158 30" height="30" preserveAspectRatio="none">
      <path d="M0 14 C50 2 100 30 158 8 V30 H0Z" fill="var(--purple)"/>
      <path d="M0 11 C50 -1 100 27 158 5" fill="none" stroke="var(--green)" stroke-width="2"/>
    </svg>
  </section>

  <!-- Business card backs -->
  <section class="sheet card card-back-purple">
    <span class="brand on-dark"><span class="dot"></span>sunlanejourneys</span>
    <svg class="wave" viewBox="0 0 158 30" height="30" preserveAspectRatio="none">
      <path d="M0 16 C50 4 100 30 158 10" fill="none" stroke="var(--green)" stroke-width="2"/>
    </svg>
  </section>
  <section class="sheet card card-back-white">
    <span class="brand"><span class="dot"></span>sunlanejourneys</span>
  </section>
  <section class="sheet card card-back-green">
    <span class="brand on-dark"><span class="dot"></span>sunlanejourneys</span>
  </section>

  <!-- Letterhead -->
  <section class="sheet letterhead">
    <span class="brand"><span class="dot"></span>sunlanejourneys</span>
    <span class="ghost-mark" aria-hidden="true">sunlanejourneys</span>
    <svg class="wave" viewBox="0 0 398 90" height="90" preserveAspectRatio="none">
      <path d="M0 30 C120 0 260 60 398 18 V90 H0Z" fill="var(--purple)"/>
      <path d="M0 26 C120 -4 260 56 398 14" fill="none" stroke="var(--green)" stroke-width="4"/>
      <path d="M0 22 C120 -8 260 52 398 10" fill="none" stroke="#d8f0c4" stroke-width="1"/>
    </svg>
    <div class="footer-info">
      <p>100 Example Street, Suite 1<br>Sampletown, ON A1A 1A1</p>
      <p>T: 905.555.0142<br>F: 905.555.0143<br>Calvin@sunlanejourneys.example</p>
    </div>
    <p class="footer-web">www.sunlanejourneys.example</p>
  </section>

  <!-- Envelope front -->
  <section class="sheet envelope">
    <span class="brand"><span class="dot"></span>sunlanejourneys</span>
    <span class="ghost-mark" aria-hidden="true">sunlanejourneys</span>
    <svg class="wave" viewBox="0 0 394 64" height="64" preserveAspectRatio="none">
      <path d="M0 26 C120 0 260 50 394 16 V64 H0Z" fill="var(--purple)"/>
      <path d="M0 22 C120 -4 260 46 394 12" fill="none" stroke="var(--green)" stroke-width="3"/>
    </svg>
    <div class="footer-info">
      <p>100 Example Street, Suite 1<br>Sampletown, ON A1A 1A1</p>
      <p>T: 905.555.0142<br>Calvin@sunlanejourneys.example</p>
    </div>
  </section>

  <!-- Envelope flaps -->
  <section class="flap flap-purple">
    <svg viewBox="0 0 394 72" preserveAspectRatio="none">
      <path d="M0 0 H394 V14 C300 74 94 74 0 14Z" fill="var(--purple)"/>
    </svg>
    <span class="brand on-dark"><span class="dot"></span>sunlanejourneys</span>
  </section>
  <section class="flap flap-green">
    <svg viewBox="0 0 394 72" preserveAspectRatio="none">
      <path d="M0 0 H394 V14 C300 74 94 74 0 14Z" fill="var(--green)"/>
    </svg>
    <span class="brand on-dark"><span class="dot"></span>sunlanejourneys</span>
  </section>
  <section class="flap flap-white">
    <svg viewBox="0 0 394 72" preserveAspectRatio="none">
      <path d="M0 0 H394 V14 C300 74 94 74 0 14Z" fill="var(--paper)"/>
    </svg>
    <span class="brand"><span class="dot"></span>sunlanejourneys</span>
  </section>

</body>
</html>
```